Flyer Design Project

New pest control company starting in southern maryland with the name Pest Rangers. We are going off the same kind of concept as the Phantomchasers. Our slogan is.....killing bugs its what we do best. The telephone number for the business is 240 617 9082. About us....we are a new exciting brand coming to the southern Maryland area offering a safer and more effective solution to pest control. We strive to use the safest and most effective products while providing the best and most effective service. We are a local based company with over ten years experience. As a special to all new Maryland clients we are offering the following coupons. 1. New customers get $100 off initial service which includes a termite inspection with a one year contract. 2. With a one year contract get 50 % off mosquito treatments normally $100 now $50 lawn treatments are done every 30 days. 3. Sign up before May 30th and receive lawn treatments for ticks and fleas up to half an acre included at no additional charge with a signed 1 year contract

Industry/Entity Type

It Company

```html
<!DOCTYPE html>
<html lang="en">
<head>
<meta charset="utf-8">
<title>Pest Rangers Flyer</title>
<link href="https://fonts.googleapis.com/css2?family=Roboto+Condensed:wght@700&family=Lato:wght@400&display=swap" rel="stylesheet">
<style>
  :root {
    --orange: #f7891f;
    --orange-dark: #c4610c;
    --green: #22cc0a;
    --panel-top: #555555;
    --panel-bottom: #6a6a6a;
    --ink: #2b2b2b;
    --white: #ffffff;
    --backdrop: #e6e6e6;
  }
  * { margin: 0; padding: 0; box-sizing: border-box; }
  html, body { width: 1200px; height: 1200px; overflow: hidden; background: var(--backdrop); }
  .canvas { position: relative; width: 1200px; height: 1200px; }
  .flyer {
    position: absolute; left: 176px; top: 59px;
    width: 1059px; height: 1353px;
    background: var(--white);
    transform: scale(0.8); transform-origin: top left;
    overflow: hidden;
  }
  .flyer > * { position: absolute; }
  .waves { left: 0; top: 0; width: 1059px; height: 1353px; }

  .headline {
    left: 40px; top: 40px; white-space: nowrap;
    font-family: "Roboto Condensed", sans-serif; font-weight: 700;
    font-size: 104px; line-height: 1; color: var(--orange);
  }
  .slogan {
    left: 40px; top: 154px; white-space: nowrap;
    font-family: "Roboto Condensed", sans-serif; font-weight: 700;
    font-size: 70px; line-height: 1; color: var(--green);
  }

  .art-bugs { left: 108px; top: 243px; width: 245px; height: 170px; border-radius: 50%;
    background: linear-gradient(135deg, #8a9a4a, #4e5a2a); }
  .art-spray { left: 383px; top: 243px; width: 310px; height: 175px; border-radius: 40px;
    background: linear-gradient(90deg, #d6d6d6, #cfd2d4 55%, #3aa55a); }
  .art-exterminator { left: 695px; top: 13px; width: 300px; height: 480px; border-radius: 40px;
    background: linear-gradient(180deg, #d8403a 0%, #e8d84a 30%, #3c56a8 65%, #cfcfcf 100%); }

  .brand-ring { left: 603px; top: 450px; width: 336px; height: 336px; border-radius: 50%;
    border: 14px solid var(--green); background: var(--white); }
  .brand-name {
    left: 547px; top: 693px; width: 460px; text-align: center;
    font-family: "Roboto Condensed", sans-serif; font-weight: 700;
    font-size: 66px; line-height: 1; color: var(--ink); white-space: nowrap;
  }
  .brand-name span { background: var(--white); padding: 0 6px; }

  .offer-panel {
    left: 40px; top: 608px; width: 448px; height: 760px;
    border-radius: 56px 56px 0 0;
    background: linear-gradient(180deg, var(--panel-top), var(--panel-bottom));
  }
  .ribbon-fold { top: 731px; width: 0; height: 0; border-top: 27px solid var(--orange-dark); }
  .ribbon-fold.left { left: 13px; border-left: 27px solid transparent; }
  .ribbon-fold.right { left: 489px; border-right: 27px solid transparent; }
  .ribbon {
    left: 13px; top: 658px; width: 503px; height: 73px;
    background: var(--orange); color: var(--white); text-align: center;
    font-family: "Roboto Condensed", sans-serif; font-weight: 700;
    font-size: 34px; line-height: 30px; padding-top: 7px;
  }

  .offer { left: 68px; width: 386px;
    font-family: "Lato", sans-serif; font-size: 25px; line-height: 31.5px; color: var(--white); }
  .offer.one { top: 756px; }
  .offer.two { top: 944px; }
  .offer.three { top: 1133px; }
  .line { display: block; white-space: nowrap; text-align: justify; text-align-last: justify; }
  .line.end { text-align: center; text-align-last: center; }
  .divider { left: 58px; width: 412px; border-top: 2px dashed #d5d5d5; }
  .divider.one { top: 920px; }
  .divider.two { top: 1108px; }

  .about-title {
    left: 559px; top: 825px;
    font-family: "Roboto Condensed", sans-serif; font-weight: 700;
    font-size: 39px; line-height: 1; color: var(--green);
  }
  .about-text { left: 560px; top: 884px; width: 419px;
    font-family: "Lato", sans-serif; font-size: 21px; line-height: 27.5px; color: #222; }
  .about-text .line.end { text-align: left; text-align-last: left; }

  .call-box {
    left: 605px; top: 1135px; width: 311px; height: 118px;
    border: 2px solid #555; border-radius: 40px; background: var(--white);
    font-family: "Roboto Condensed", sans-serif; font-weight: 700; text-align: center;
  }
  .call-label { position: absolute; left: 0; right: 0; top: 10px; font-size: 38px; line-height: 1; color: var(--green); }
  .call-number { position: absolute; left: 0; right: 0; top: 48px; font-size: 51px; line-height: 1; color: var(--ink); }
</style>
</head>
<body>
<div class="canvas">
  <div class="flyer">
    <svg class="waves" viewBox="0 0 1059 1353" aria-hidden="true">
      <path d="M0,513 C120,420 230,385 330,393 C450,402 560,470 680,525 L690,560 C560,505 440,450 320,445 C200,440 90,520 0,628 Z" fill="var(--green)"/>
      <path d="M0,645 C110,525 220,465 330,465 C470,468 600,540 720,590 C820,625 920,610 1059,570 L1059,630 C930,680 820,680 720,650 C590,610 460,490 320,488 C200,490 90,560 0,660 Z" fill="var(--orange)"/>
      <path d="M0,1160 C300,1150 640,1230 860,1225 C960,1222 1020,1185 1059,1150" fill="none" stroke="var(--green)" stroke-width="16"/>
      <path d="M0,1210 C300,1210 640,1290 860,1290 C960,1288 1020,1220 1059,1168 L1059,1353 L0,1353 Z" fill="var(--orange)"/>
    </svg>

    <div class="headline">KILLING BUGS</div>
    <div class="slogan">ITS WHAT WE DO BEST</div>

    <div class="art-bugs" role="img" aria-label="Cartoon bugs running away"></div>
    <div class="art-spray" role="img" aria-label="Cloud of pesticide spray from a hose nozzle"></div>
    <div class="art-exterminator" role="img" aria-label="Cartoon exterminator in cap and overalls holding a spray tank"></div>

    <div class="brand-ring"></div>
    <div class="brand-name"><span>PEST RANGERS</span></div>

    <div class="offer-panel"></div>
    <div class="ribbon-fold left"></div>
    <div class="ribbon-fold right"></div>
    <div class="ribbon">SPECIAL OFFER TO ALL NEW<br>MARYLAND CLIENTS</div>

    <p class="offer one">
      <span class="line">New customers get $100 off</span>
      <span class="line">initial service which includes a</span>
      <span class="line">termite inspection with a one year</span>
      <span class="line end">contract.</span>
    </p>
    <div class="divider one"></div>
    <p class="offer two">
      <span class="line">With a one year contract get 50 %</span>
      <span class="line">off mosquito treatments normally</span>
      <span class="line">$100 now $50 lawn treatments</span>
      <span class="line end">are done every 30 days.</span>
    </p>
    <div class="divider two"></div>
    <p class="offer three">
      <span class="line">Sign up before May 30th and</span>
      <span class="line">receive lawn treatments for ticks</span>
      <span class="line">and fleas up to half an acre</span>
      <span class="line">included at no additional charge</span>
      <span class="line end">with a signed 1 year contract</span>
    </p>

    <h2 class="about-title">ABOUT US</h2>
    <p class="about-text">
      <span class="line">We are a new exciting brand coming to the</span>
      <span class="line">southern Maryland area offering a safer</span>
      <span class="line">and more effective solution to pest</span>
      <span class="line">control. We strive to use the safest and</span>
      <span class="line">most effective products while providing</span>
      <span class="line">the best and most effective service. We</span>
      <span class="line">are a local based company with over ten</span>
      <span class="line end">years experience.</span>
    </p>

    <div class="call-box">
      <span class="call-label">CALL US NOW</span>
      <span class="call-number">240 617 9082</span>
    </div>
  </div>
</div>
</body>
</html>
```